Family Owned and Operated Spray Foam Insulation Company needs a business card design

We're a new company based in the heart of Texas (Fort Worth). We spray foam insulation into residential houses, commercial buildings, metal buildings, etc. Spray foam insulation provides a huge reduction in energy/costs so that is what drives our market. We like the primary colors but are open to suggestions and are coming to the experts for some creativity. I'm attaching a picture of shirt mock up we have with KLB on the front to show what we were leaning towards as well as some business cards that I find striking and memorable. I'm looking for a card that is clean and professional with a bit of edge. Note: My computer won't pull up the color samples below for me to choose so it's in your hands.

Target Market(s)

Professional custom home builders, construction industry, home owners

Industry/Entity Type

Residential

Contact Information for Business Card

Name: Marcus Kettle (no title) Phone #: 817-555-0148, address: 4087 larkmoor ave fort worth tx 76110, email: marcus@klbinsulation-example.com, website: klbinsulation-example.com

Requirements
Must have
• We want the words KLB and Kettle Spray Foam Insulation showcased on the card but hopefully on opposite sides
Should not have
• Any type of spray foam gun or splatter clip art

```html
<!DOCTYPE html>
<html lang="en">
<head>
<meta charset="utf-8">
<title>Kettle Spray Foam Insulation – Business Card</title>
<link rel="stylesheet" href="https://fonts.googleapis.com/css2?family=Oswald:wght@600;700&family=Open+Sans:wght@400&display=swap">
<style>
  :root {
    --page-bg: #dcdcdc;
    --card-back: #141622;
    --card-front: #f7f6f4;
    --brand-red: #a8272c;
    --brand-navy: #283049;
    --text-grey: #4f535c;
    --watermark: #ecd3d4;
  }
  * { margin: 0; padding: 0; box-sizing: border-box; }
  html, body {
    width: 1200px;
    height: 900px;
    overflow: hidden;
    background: var(--page-bg);
  }
  .canvas {
    position: relative;
    width: 1200px;
    height: 900px;
  }
  .card {
    position: absolute;
    left: 285px;
    width: 630px;
    height: 360px;
    border-radius: 4px;
    box-shadow: 0 6px 18px rgba(0, 0, 0, 0.18);
    overflow: hidden;
  }
  .card--back {
    top: 60px;
    background: var(--card-back);
    display: flex;
    align-items: center;
    justify-content: center;
  }
  .card--front {
    top: 480px;
    background: var(--card-front);
  }
  .wordmark {
    font-family: "Oswald", sans-serif;
    font-weight: 700;
    color: var(--brand-red);
    letter-spacing: 2px;
    line-height: 1;
  }
  .card--back .wordmark { font-size: 64px; }
  .identity {
    position: absolute;
    left: 44px;
    top: 42px;
  }
  .identity .wordmark { font-size: 52px; }
  .person-name {
    margin-top: 6px;
    font-family: "Oswald", sans-serif;
    font-weight: 600;
    font-size: 19px;
    letter-spacing: 1.5px;
    color: var(--brand-navy);
    text-transform: uppercase;
  }
  .company-block {
    position: absolute;
    right: 40px;
    top: 56px;
    text-align: center;
  }
  .company-name {
    font-family: "Oswald", sans-serif;
    font-weight: 600;
    font-size: 17px;
    letter-spacing: 1.5px;
    color: var(--brand-navy);
    text-transform: uppercase;
  }
  .company-watermark {
    font-family: "Oswald", sans-serif;
    font-weight: 700;
    font-size: 120px;
    line-height: 1;
    letter-spacing: 4px;
    color: var(--watermark);
  }
  .contact-list {
    position: absolute;
    left: 44px;
    bottom: 40px;
    list-style: none;
    font-family: "Open Sans", sans-serif;
    font-weight: 400;
    font-size: 19px;
    line-height: 1.3;
    color: var(--text-grey);
  }
</style>
</head>
<body>
  <main class="canvas">
    <section class="card card--back" aria-label="Business card back">
      <span class="wordmark">KLB</span>
    </section>

    <section class="card card--front" aria-label="Business card front">
      <div class="identity">
        <div class="wordmark">KLB</div>
        <div class="person-name">Marcus Kettle</div>
      </div>

      <div class="company-block">
        <div class="company-name">Kettle Spray Foam Insulation</div>
        <div class="company-watermark" aria-hidden="true">KLB</div>
      </div>

      <ul class="contact-list">
        <li>817-555-0148</li>
        <li>marcus@klbinsulation-example.com</li>
        <li>klbinsulation-example.com</li>
        <li>4087 larkmoor ave fort worth tx 76110</li>
      </ul>
    </section>
  </main>
</body>
</html>
```